Design a 1-page brochure with our "The Harbinger Pathway" illustrated.

i have included my logo, an outline of the text and name of each step, and a quick sketch of generally how i would like the image to look. But please make it look sexy.

Each step should include the subtext as shown on the pdf attached. i.e. The first part of the image (far left) is "Problems", under that should list : 1. Poor Expectations; 2. Poor Communication... and so on for all the steps included.

I have also included a previous brochure that shows our branding and style.

Target Market(s)

Restaurant, Retail, Commercial

Industry/Entity Type

Construction Management

Font styles to use
Sans Serif

Colors
EB3D1F
EC4F4E
F09395
F8D3D4
FCEDEE

Requirements
Must have
• Our logo. Title of graphic: The Harbinger Pathway, our website and IG. www.quorvanbuildco.example. @quorvanbuildco

```html
<!DOCTYPE html>
<html lang="en">
<head>
<meta charset="utf-8">
<title>The Harbinger Pathway – Quorvan Build Co</title>
<link href="https://fonts.googleapis.com/css2?family=Montserrat:wght@400;500;600;700;800&display=swap" rel="stylesheet">
<style>
  :root {
    --ink: #1c1c1f;
    --red: #eb2a2f;
    --red-deep: #9e1a1f;
    --red-mid: #c3222a;
    --bullet: #f09395;
    --white: #ffffff;
    --text: #f4f4f4;
  }
  * { margin: 0; padding: 0; box-sizing: border-box; }
  html, body { width: 933px; height: 1200px; overflow: hidden; background: var(--ink); }
  body { font-family: "Montserrat", sans-serif; color: var(--text); }
  .brochure { position: relative; width: 933px; height: 1200px; background: var(--ink); overflow: hidden; }
  .hero-photo, .pathway-graphic { position: absolute; left: 0; top: 0; width: 933px; height: 760px; }
  .brand { position: absolute; left: 38px; top: 44px; width: 150px; text-align: center; }
  .brand-mark { display: block; width: 58px; height: 58px; margin: 0 auto 12px; background: var(--red); }
  .brand-name { font-weight: 700; font-size: 11px; letter-spacing: 0.4px; color: var(--white); white-space: nowrap; }
  .step { position: absolute; }
  .step-title { font-weight: 600; font-size: 26px; line-height: 1.1; color: var(--red); margin-bottom: 6px; }
  .step-list { list-style: none; }
  .step-list li { position: relative; padding-left: 15px; font-size: 14.5px; line-height: 18px; margin-bottom: 6px; }
  .step-list li::before { content: ""; position: absolute; left: 1px; top: 6px; width: 6px; height: 6px; border-radius: 50%; background: var(--bullet); }
  .step-possibility { left: 705px; top: 262px; width: 215px; }
  .step-complete { left: 570px; top: 388px; width: 120px; }
  .step-manage { left: 460px; top: 503px; width: 210px; }
  .step-execute { left: 329px; top: 617px; width: 160px; }
  .step-organize { left: 209px; top: 737px; width: 190px; }
  .step-organize .step-list li { margin-bottom: 6px; }
  .step-problems { left: 50px; top: 758px; width: 180px; }
  .step-problems .step-list { margin-top: 10px; }
  .pathway-title { position: absolute; left: 518px; top: 752px; font-weight: 800; line-height: 68px; font-size: 60px; letter-spacing: -1px; color: var(--white); }
  .pathway-title .lead { color: var(--red); display: block; }
  .pathway-title span { display: block; }
  .contact { position: absolute; left: 0; top: 1030px; width: 933px; height: 170px; }
  .contact-title { position: absolute; left: 128px; top: 12px; font-weight: 600; font-size: 25px; color: var(--red); }
  .contact-rule { position: absolute; left: 0; top: 0; width: 933px; height: 170px; }
  .contact-item { position: absolute; top: 66px; font-size: 14.5px; line-height: 18px; color: var(--text); }
  .contact-web { left: 128px; }
  .contact-ig { left: 393px; }
  .contact-name { left: 632px; text-transform: uppercase; }
</style>
</head>
<body>
<main class="brochure">
  <svg class="hero-photo" viewBox="0 0 933 760" role="img" aria-label="Photo of a construction planner sketching on blueprints beside a yellow hard hat and notebooks">
    <defs>
      <linearGradient id="photoTone" x1="0" y1="0" x2="1" y2="1">
        <stop offset="0" stop-color="#8a8788"/>
        <stop offset="0.35" stop-color="#a99a8a"/>
        <stop offset="0.55" stop-color="#6f6a6e"/>
        <stop offset="1" stop-color="#3e4146"/>
      </linearGradient>
      <radialGradient id="hatGlow" cx="0.32" cy="0.5" r="0.25">
        <stop offset="0" stop-color="#d9b24a" stop-opacity="0.55"/>
        <stop offset="1" stop-color="#d9b24a" stop-opacity="0"/>
      </radialGradient>
    </defs>
    <polygon points="0,0 933,0 933,44 189,736 0,736" fill="url(#photoTone)"/>
    <polygon points="0,0 933,0 933,44 189,736 0,736" fill="url(#hatGlow)"/>
  </svg>

  <svg class="pathway-graphic" viewBox="0 0 933 760" aria-hidden="true">
    <defs>
      <linearGradient id="hexFill" x1="0" y1="0" x2="1" y2="1">
        <stop offset="0" stop-color="#c3222a"/>
        <stop offset="1" stop-color="#8e171c"/>
      </linearGradient>
      <g id="hex">
        <polygon points="0,-52 45,-26 45,26 0,52 -45,26 -45,-26" fill="url(#hexFill)" stroke="#ffffff" stroke-width="3"/>
      </g>
      <g id="arrow">
        <line x1="-16" y1="16" x2="16" y2="-16" stroke="#c3222a" stroke-width="2"/>
        <polyline points="4,-16 16,-16 16,-4" fill="none" stroke="#c3222a" stroke-width="2"/>
      </g>
    </defs>

    <use href="#arrow" x="299" y="618"/>
    <use href="#arrow" x="425" y="500"/>
    <use href="#arrow" x="551" y="384"/>
    <use href="#arrow" x="679" y="264"/>

    <g transform="translate(243,678)">
      <use href="#hex"/>
      <g fill="none" stroke="#fff" stroke-width="2">
        <rect x="-20" y="-26" width="40" height="52" rx="1"/>
        <polyline points="-13,-14 -10,-11 -5,-17"/><line x1="-1" y1="-14" x2="13" y2="-14"/>
        <polyline points="-13,-1 -10,2 -5,-4"/><line x1="-1" y1="-1" x2="13" y2="-1"/>
        <polyline points="-13,12 -10,15 -5,9"/><line x1="-1" y1="12" x2="13" y2="12"/>
      </g>
    </g>

    <g transform="translate(360,563)">
      <use href="#hex"/>
      <g fill="none" stroke="#fff" stroke-width="2" stroke-linejoin="round">
        <polyline points="-24,22 -12,22 -12,10 0,10 0,-2 12,-2 12,-14 24,-14"/>
        <line x1="18" y1="-14" x2="18" y2="-28"/>
        <polygon points="18,-28 28,-24 18,-20"/>
      </g>
    </g>

    <g transform="translate(490,445)">
      <use href="#hex"/>
      <g fill="none" stroke="#fff" stroke-width="2" stroke-linejoin="round">
        <path d="M-26,-18 h28 v18 h-16 l-8,7 v-7 h-4 z"/>
        <path d="M26,-6 h-22 v16 h12 l7,6 v-6 h3 z"/>
      </g>
    </g>

    <g transform="translate(616,328)">
      <use href="#hex"/>
      <g fill="none" stroke="#fff" stroke-width="2.4" stroke-linejoin="round">
        <line x1="-10" y1="-22" x2="-10" y2="22"/>
        <path d="M-10,-22 q6,-4 12,0 t14,0 v16 q-7,4 -14,0 t-12,0"/>
        <line x1="-14" y1="22" x2="-6" y2="22"/>
      </g>
    </g>

    <g transform="translate(741,211)">
      <use href="#hex"/>
      <g fill="none" stroke="#fff" stroke-width="2" stroke-linejoin="round">
        <circle cx="0" cy="-8" r="17"/>
        <circle cx="0" cy="-8" r="11"/>
        <polygon points="0,-15 2,-10 7,-10 3,-7 5,-2 0,-5 -5,-2 -3,-7 -7,-10 -2,-10"/>
        <polyline points="-10,6 -18,24 -11,21 -7,28 -2,9"/>
        <polyline points="10,6 18,24 11,21 7,28 2,9"/>
      </g>
    </g>
  </svg>

  <div class="brand">
    <span class="brand-mark"></span>
    <span class="brand-name">QUORVAN BUILD CO</span>
  </div>

  <section class="step step-possibility">
    <h2 class="step-title">Possibility</h2>
    <ul class="step-list">
      <li>Project Synergy</li>
      <li>Excellent Communication where budget and Schedule are visible and approved</li>
      <li>Clear project visibility where everyone understands how we get to a successful end</li>
      <li>Everyone involved is proud of the final product</li>
    </ul>
  </section>

  <section class="step step-complete">
    <h2 class="step-title">Complete</h2>
    <ul class="step-list"><li>Project Closeout</li></ul>
  </section>

  <section class="step step-manage">
    <h2 class="step-title">Manage</h2>
    <ul class="step-list">
      <li>O.O.D.A</li>
      <li>Shared Consciousness Meetings</li>
      <li>Pressurized Collaboration</li>
    </ul>
  </section>

  <section class="step step-execute">
    <h2 class="step-title">Execute</h2>
    <ul class="step-list"><li>Project Start</li></ul>
  </section>

  <section class="step step-organize">
    <h2 class="step-title">Organize</h2>
    <ul class="step-list">
      <li>Develop Project Plan</li>
      <li>Develop Schedule</li>
      <li>Develop Budget</li>
    </ul>
  </section>

  <section class="step step-problems">
    <h2 class="step-title">Common<br>Problems</h2>
    <ul class="step-list">
      <li>Changing or poor expectations</li>
      <li>Poor communication</li>
      <li>No Journey to Success</li>
      <li>No Trust</li>
      <li>No Accountability</li>
    </ul>
  </section>

  <h1 class="pathway-title">
    <span class="lead">The</span>
    <span>Harbinger</span>
    <span>Pathway</span>
  </h1>

  <footer class="contact">
    <svg class="contact-rule" viewBox="0 0 933 170" aria-hidden="true">
      <line x1="59" y1="49" x2="731" y2="49" stroke="#eb2a2f" stroke-width="1.6"/>
      <line x1="808" y1="49" x2="875" y2="49" stroke="#eb2a2f" stroke-width="1.6"/>
      <circle cx="769" cy="48" r="30" fill="none" stroke="#c3222a" stroke-width="1.6"/>
      <rect x="766" y="37" width="6" height="22" fill="#c3222a"/>
      <rect x="766" y="29" width="6" height="5" fill="#c3222a"/>
      <polyline points="355,64 357,64 357,82 362,87 357,92 357,103 355,103" fill="none" stroke="#c3222a" stroke-width="1.4"/>
      <polyline points="595,64 597,64 597,82 602,87 597,92 597,103 595,103" fill="none" stroke="#c3222a" stroke-width="1.4"/>
    </svg>
    <h2 class="contact-title">Contact us</h2>
    <p class="contact-item contact-web">Visit our website:<br>www.quorvanbuildco.example</p>
    <p class="contact-item contact-ig">Follow us on IG<br>@quorvanbuildco</p>
    <p class="contact-item contact-name">Quorvan<br>Build Co</p>
  </footer>
</main>
</body>
</html>
```